Bref créative
Valcourt Chiropractic
Business card, letterhead, envelope
Professional
Valcourt Chiropractic (use logo)
41785 Brookhaven Rd
Oakridge Twp, MI 48193
info@ValcourtChiroExample.com
www.ValcourtChiroExample.com
Want a design that portrays health and wellness in a professional manner
(in bullet format)
-We Specialize in Improving Health & Wellness Naturally
-Most Insurances Accepted
-Holistic Family Health Care
-Massage Therapist on Staff

```html
<!DOCTYPE html>
<html lang="en">
<head>
<meta charset="utf-8">
<title>Valcourt Chiropractic — Stationery</title>
<link rel="stylesheet" href="https://fonts.googleapis.com/css2?family=Open+Sans:wght@400;600&display=swap">
<style>
  :root {
    --green: #5a8f32;
    --blue: #1f4d9c;
    --ink: #4a4a4a;
    --paper: #ffffff;
    --frame: #e4e4e4;
    --edge: #d6d6d6;
    --faint: #f1f5ee;
  }
  * { box-sizing: border-box; margin: 0; padding: 0; }
  html, body {
    width: 1200px; height: 681px; overflow: hidden;
    background: var(--paper);
    font-family: "Open Sans", Arial, sans-serif;
    color: var(--ink);
  }
  .board {
    position: absolute; left: 20px; top: 20px; width: 1160px; height: 630px;
    border: 1px solid var(--frame);
  }
  .piece {
    position: absolute; background: var(--paper);
    border: 1px solid var(--edge); overflow: hidden;
    box-shadow: 2px 3px 6px rgba(0,0,0,.12);
  }
  .header-wave { position: absolute; top: 0; right: 0; }

  .brand { position: absolute; display: flex; align-items: center; gap: 7px; white-space: nowrap; }
  .brand-dot { border-radius: 50%; background: var(--green); flex: none; }
  .brand-name {
    font-family: "Open Sans", Arial, sans-serif; font-weight: 600;
    color: var(--blue); line-height: 1;
  }

  .envelope-front { left: 48px; top: 44px; width: 456px; height: 184px; }
  .envelope-front .brand { left: 20px; top: 20px; }
  .envelope-front .brand-dot { width: 26px; height: 26px; }
  .envelope-front .brand-name { font-size: 14px; }
  .return-address { position: absolute; left: 22px; top: 56px; font-size: 6px; }

  .envelope-back { left: 48px; top: 312px; width: 456px; height: 184px; }
  .flap-line { position: absolute; inset: 0; }
  .seal-dot {
    position: absolute; left: 216px; top: 82px; width: 24px; height: 24px;
    border-radius: 50%; background: var(--green);
  }

  .letterhead { left: 619px; top: 44px; width: 322px; height: 576px; }
  .letterhead .brand { left: 18px; top: 20px; }
  .letterhead .brand-dot { width: 24px; height: 24px; }
  .letterhead .brand-name { font-size: 13px; }
  .letterhead-contact {
    position: absolute; left: 20px; top: 54px; font-size: 5px; line-height: 1.5;
  }
  .faint-circle {
    position: absolute; left: 200px; top: 418px; width: 110px; height: 110px;
    border-radius: 50%; background: var(--faint);
  }

  .card { width: 185px; height: 104px; left: 967px; }
  .card-front { top: 168px; }
  .card-back { top: 293px; }
  .card .brand { left: 9px; top: 14px; gap: 4px; }
  .card .brand-dot { width: 14px; height: 14px; }
  .card .brand-name { font-size: 7.5px; }
  .card-details {
    position: absolute; left: 10px; top: 38px; font-size: 4.4px; line-height: 1.55;
  }
  .card-details ul { list-style: none; }
</style>
</head>
<body>
<main class="board">

  <section class="piece envelope-front" aria-label="Envelope front">
    <svg class="header-wave" width="456" height="92" viewBox="0 0 300 60" preserveAspectRatio="none" aria-hidden="true">
      <path d="M120 0 H300 V42 C240 38 170 22 120 0 Z" fill="var(--green)"/>
      <path d="M92 0 C150 30 220 44 300 50" fill="none" stroke="var(--blue)" stroke-width="2"/>
    </svg>
    <div class="brand">
      <span class="brand-dot"></span>
      <span class="brand-name">Valcourt Chiropractic</span>
    </div>
    <p class="return-address">41785 Brookhaven Rd · Oakridge Twp, MI 48193</p>
  </section>

  <section class="piece envelope-back" aria-label="Envelope back">
    <svg class="flap-line" width="456" height="184" viewBox="0 0 456 184" aria-hidden="true">
      <path d="M0 4 L190 84 Q228 100 266 84 L456 4" fill="none" stroke="var(--edge)" stroke-width="1.5"/>
    </svg>
    <span class="seal-dot"></span>
  </section>

  <section class="piece letterhead" aria-label="Letterhead">
    <svg class="header-wave" width="322" height="76" viewBox="0 0 300 60" preserveAspectRatio="none" aria-hidden="true">
      <path d="M100 0 H300 V42 C230 38 160 22 100 0 Z" fill="var(--green)"/>
      <path d="M70 0 C140 30 215 44 300 50" fill="none" stroke="var(--blue)" stroke-width="2"/>
    </svg>
    <div class="brand">
      <span class="brand-dot"></span>
      <span class="brand-name">Valcourt Chiropractic</span>
    </div>
    <div class="letterhead-contact">
      <p>41785 Brookhaven Rd, Oakridge Twp, MI 48193</p>
      <p>Phone (586) 555-0142, Fax (586) 555-0143</p>
      <p>info@ValcourtChiroExample.com · www.ValcourtChiroExample.com</p>
    </div>
    <span class="faint-circle"></span>
  </section>

  <section class="piece card card-front" aria-label="Business card front">
    <svg class="header-wave" width="185" height="40" viewBox="0 0 300 60" preserveAspectRatio="none" aria-hidden="true">
      <path d="M120 0 H300 V42 C240 38 170 22 120 0 Z" fill="var(--green)"/>
      <path d="M92 0 C150 30 220 44 300 50" fill="none" stroke="var(--blue)" stroke-width="2.5"/>
    </svg>
    <div class="brand">
      <span class="brand-dot"></span>
      <span class="brand-name">Valcourt Chiropractic</span>
    </div>
    <div class="card-details">
      <p>Renee Valcourt, D.C.</p>
      <p>Doctor of Chiropractic</p>
      <p>T (586) 555-0142</p>
      <p>F (586) 555-0143</p>
      <p>rvalcourt@ValcourtChiroExample.com</p>
    </div>
  </section>

  <section class="piece card card-back" aria-label="Business card back">
    <svg class="header-wave" width="185" height="40" viewBox="0 0 300 60" preserveAspectRatio="none" aria-hidden="true">
      <path d="M120 0 H300 V42 C240 38 170 22 120 0 Z" fill="var(--green)"/>
      <path d="M92 0 C150 30 220 44 300 50" fill="none" stroke="var(--blue)" stroke-width="2.5"/>
    </svg>
    <div class="card-details">
      <ul>
        <li>• We Specialize in Improving Health &amp; Wellness Naturally</li>
        <li>• Most Insurances Accepted</li>
        <li>• Holistic Family Health Care</li>
        <li>• Massage Therapist on Staff</li>
      </ul>
    </div>
  </section>

</main>
</body>
</html>
```